I need a business card representing my company, VELDRA, it's an artist management and design company. Complete name is "VELDRA Artist Mgmt. + Design Co." I need it to be world class and very appealing, sophisticated and artistically unique.
Updates

Posted an updated Brief please see. I need a business card representing my company, VELDRA, it's an artist management and design company. Complete name is "VELDRA Artist Mgmt. + Design Co." I need it to be world class and very appealing, sophisticated and artistically unique.

Designs look the same

Designs look the same

Target Market(s)

Advertisers, Entertainment Companies, Commercial companies

Industry/Entity Type

Advertising

Contact Information for Business Card

I need a business card representing my company, VELDRA, it's an artist management and design company. Complete name is "VELDRA Artist Mgmt. + Design Co." I need it to be world class and very appealing, sophisticated and artistically unique. One side can be VELDRA Artist Mgmt. + Design Co. and the other my name, Teodoro Lindqvist, my contact telephone: 412.638.2957, email veldraartist@plumora.net, my address: 3264 Harwell Ave. #517 Miami, FL 33184

Font styles to use
Other font styles liked:
• Calibri

Colors
ffffff
0455a3
f37122

Requirements
Must have
• "VELDRA" stand out bigger than the rest of the text.
Nice to have
• Name "VELDRA" can be centered on one side or in the corner or along side edges, just need something cool and different.
Should not have
• I am open just try to keep it clean looking

```html
<!DOCTYPE html>
<html lang="en">
<head>
<meta charset="utf-8">
<title>VELDRA Artist Mgmt. + Design Co. — Business Card</title>
<link rel="stylesheet" href="https://fonts.googleapis.com/css2?family=Arimo:wght@400&family=Open+Sans:wght@400&display=swap">
<style>
  :root {
    --card-bg: #ffffff;
    --ink: #111111;
    --brand-blue: #0455a3;
    --accent-orange: #ec9708;
  }
  html, body {
    margin: 0;
    padding: 0;
    width: 1200px;
    height: 1000px;
    overflow: hidden;
    background: var(--card-bg);
  }
  .card {
    position: relative;
    width: 1200px;
    height: 1000px;
    background: var(--card-bg);
    color: var(--ink);
    overflow: hidden;
  }
  .card > * {
    position: absolute;
    margin: 0;
    line-height: 1;
    white-space: nowrap;
    font-weight: 400;
  }
  .humanist { font-family: "Open Sans", "Segoe UI", sans-serif; }
  .grotesk { font-family: "Arimo", Arial, sans-serif; }

  .holder-name { left: 97px; top: 51px; font-size: 54px; }
  .holder-email { left: 158px; top: 136px; font-size: 36px; }

  .brand-mark {
    left: 760px; top: 232px;
    width: 90px; height: 90px;
    background: var(--accent-orange);
  }
  .brand-name {
    left: 618px; top: 326px;
    font-size: 132px;
    color: var(--brand-blue);
  }
  .brand-descriptor { left: 626px; top: 472px; font-size: 34px; }
  .brand-site { left: 672px; top: 535px; font-size: 58px; }

  .street-number { left: 103px; top: 585px; font-size: 118px; }
  .address-line { left: 110px; }
  .address-street { top: 726px; font-size: 50px; }
  .address-suite { top: 804px; font-size: 48px; }
  .address-city { top: 881px; font-size: 44px; }

  .phone-line { left: 657px; }
  .phone-office { top: 726px; font-size: 52px; }
  .phone-direct { top: 801px; font-size: 52px; }
  .phone-fax { top: 871px; font-size: 58px; }
</style>
</head>
<body>
  <main class="card">
    <p class="holder-name humanist">Teodoro Lindqvist</p>
    <p class="holder-email humanist">tlindqvist@veldraart.net</p>

    <div class="brand-mark" aria-hidden="true"></div>
    <p class="brand-name humanist">VELDRA</p>
    <p class="brand-descriptor humanist">Artist Mgmt. + Design Co.</p>
    <p class="brand-site humanist">veldraart.net</p>

    <p class="street-number grotesk">3264</p>
    <p class="address-line address-street grotesk">Harwell Avenue</p>
    <p class="address-line address-suite grotesk">Studio 517</p>
    <p class="address-line address-city grotesk">Miami,&nbsp; Florida 33184</p>

    <p class="phone-line phone-office grotesk">Office 412.638.2900</p>
    <p class="phone-line phone-direct grotesk">Direct 412.638.2957</p>
    <p class="phone-line phone-fax grotesk">Fax 412.638.2911</p>
  </main>
</body>
</html>
```